New web design for a service provider in the medical field

We are looking for a new design for our website. We are a company that repairs and sells medical endoscopes. Our customers include doctors and hospitals. Our current website can be found at https://lumenfix.example/en/lumenfix-english.
We need a new web design (without programming) for the following 3 pages:
-Startpage https://lumenfix.example/en/lumenfix-english/
-Used endoscopes https://lumenfix.example/en/used-endoscopes/
-Purchase https://lumenfix.example/en/purchase/
The design should be modern and stylish.
The blue color of the logo should be reflected on the page, but not too intrusive.
I have uploaded the images from the header. If more images are needed, let me know and I will upload them.

Target Market(s)
Doctors and hospitals

```html
<!DOCTYPE html>
<html lang="en">
<head>
<meta charset="utf-8">
<title>LumenFix – The Endoscope Expert</title>
<link rel="stylesheet" href="https://fonts.googleapis.com/css2?family=Josefin+Sans:wght@300;400;600;700&display=swap">
<style>
:root{
  --blue:#1f6fe0;
  --blue-deep:#1652b8;
  --navy:#15206b;
  --sky:#2aaaf4;
  --orange:#ff6a2b;
  --coral:#ff5f45;
  --ink:#222;
  --muted:#666;
  --grey-band:#ececec;
  --card:#efefef;
  --pale:#eef7fb;
  --white:#fff;
}
*{margin:0;padding:0;box-sizing:border-box}
html,body{width:1200px;height:4827px;overflow:hidden}
body{position:relative;font-family:'Josefin Sans',sans-serif;color:var(--ink);background:var(--white)}
.abs{position:absolute}
.center{text-align:center}
a{color:inherit;text-decoration:none}

.topbar{left:0;top:0;width:1200px;height:47px;background:linear-gradient(90deg,#1e4fc4,#2a62e6);color:#fff;font-size:14px}
.topbar span{position:absolute;top:17px}
.flag{width:20px;height:13px;background:linear-gradient(#b22234 0 15%,#fff 15% 30%,#b22234 30% 45%,#fff 45% 60%,#b22234 60% 75%,#fff 75% 90%,#b22234 90%);position:absolute}
.flag::before{content:"";position:absolute;left:0;top:0;width:9px;height:7px;background:#3c3b6e}

.nav{left:0;top:47px;width:1200px;height:69px;background:#fff}
.brand{font-weight:700;color:var(--navy);font-size:16px;display:flex;align-items:center;gap:7px}
.brand i{display:block;width:12px;height:12px;border-radius:50%;background:var(--sky)}
.nav .link{position:absolute;top:28px;font-size:14px;color:#333}
.nav .active{color:var(--blue);border-bottom:1.5px solid var(--blue);padding-bottom:2px}
.nav .shop{top:20px;left:977px;width:77px;height:30px;border-radius:15px;background:var(--sky);color:#fff;text-align:center;line-height:32px}

.hero{left:0;top:116px;width:1200px;height:630px;background:radial-gradient(ellipse at 45% 40%,#7fb2ff 0%,#3d7ff0 35%,#1d5ad8 70%,#1646b4 100%)}
.hero h1{position:absolute;top:322px;width:1200px;text-align:center;color:#fff;font-weight:700;font-size:46px}
.hero h1 em{font-style:normal;color:var(--orange)}
.hero .sub{top:377px;width:1200px;color:#fff;font-size:25px;font-weight:300}
.hero .cert{top:418px;width:1200px;color:#fff;font-size:12px;display:flex;justify-content:center;align-items:center;gap:6px}
.btn-white{left:366px;top:463px;width:470px;height:43px;border-radius:22px;background:#fff;color:#222;font-size:14px;line-height:45px}
.hero .services{top:518px;left:548px;width:104px;color:#fff;font-size:14px;border-bottom:1.5px solid #fff;padding-bottom:3px}

.brands{left:0;top:746px;width:1200px;height:71px;background:#e7e7e7}
.brandname{font-weight:700;color:#8a8a8a;letter-spacing:1px;line-height:1}
.brands .lead{left:156px;top:30px;font-size:11px;color:#777}

h2.section{font-weight:700;font-size:42px;color:#1a1a1a}
.expert .col{position:absolute;width:240px;text-align:center}
.col h3{font-weight:400;font-size:14px;color:#222;margin-top:12px}
.col p{font-size:12px;color:var(--muted);line-height:16px;margin-top:30px;padding:0 6px}
.pill{position:absolute;border-radius:16px;color:#fff;font-size:12px;font-weight:700;letter-spacing:1px;display:flex;align-items:center;justify-content:center;gap:12px}
.pill.navy{background:var(--navy)}
.pill.sky{background:var(--sky)}
.pill.coral{background:var(--coral)}

.about{left:0;top:1434px;width:1200px;height:518px;background:var(--grey-band)}
.warranty{left:128px;top:1485px;width:268px;height:66px}
.about h2{left:126px;top:1572px;font-size:45px;font-weight:700;color:var(--navy)}
.about h2 span{color:var(--sky)}
.about .tag{left:128px;top:1624px;font-size:25px;color:var(--navy)}
.about .body{left:128px;top:1664px;width:464px;font-size:11px;line-height:19.5px;color:var(--navy)}

.photo{position:absolute}
.feature{position:absolute;padding:58px 0 0 0}
.feature h3{font-size:26px;font-weight:400;color:var(--navy)}
.feature h4{font-size:14px;font-weight:400;color:#333;margin-top:6px}
.feature p{font-size:12px;color:#777;line-height:16px;width:250px;margin-top:28px}

.values{left:0;top:3536px;width:1200px;height:570px;background:linear-gradient(180deg,#1a5cc6,#1a56bb)}
.values h2{top:122px;width:1200px;color:#fff;font-size:42px;font-weight:700}
.val{position:absolute;top:232px;width:320px;text-align:center;color:#fff}
.val h3{font-weight:400;font-size:26px;margin-top:24px}
.val p{font-size:13px;line-height:16px;margin-top:14px;padding:0 18px}

.contact h2{font-size:38px;font-weight:700;color:#1a1a1a;width:600px;text-align:center}
.contact p{font-size:12.5px;color:#555;line-height:16px;width:600px;text-align:center}
.cbtn{position:absolute;top:4431px;width:465px;height:40px;border-radius:20px;background:var(--sky);color:#fff;font-size:10px;font-weight:700;letter-spacing:.5px;text-align:center;line-height:42px;box-shadow:0 6px 10px rgba(42,170,244,.35)}

.social{position:absolute;top:4672px;width:12px;height:12px;border-radius:50%;background:#555}
.foot-links{left:375px;top:4772px;font-size:10px;color:#777;display:flex;gap:20px}
.copyright{left:0;top:4796px;width:1200px;height:31px;background:#e6e6e6;font-size:10px;color:#888;text-align:center;line-height:32px}
</style>
</head>
<body>

<header class="abs topbar">
  <span style="left:870px">pick-up order</span>
  <span style="left:993px">about us</span>
  <span style="left:1096px;font-size:9px">▾</span>
  <i class="flag" style="left:1113px;top:15px"></i>
</header>

<nav class="abs nav">
  <div class="abs brand" style="left:88px;top:26px"><i></i>LumenFix</div>
  <a class="link active" style="left:555px">Home</a>
  <a class="link" style="left:646px">Repair</a>
  <a class="link" style="left:753px">Systems</a>
  <a class="link" style="left:860px">Accessories</a>
  <a class="abs shop">Shop</a>
  <a class="link" style="left:1090px">Contact</a>
</nav>

<section class="abs hero" role="img" aria-label="Close-up photo of an endoscope control body in blue light">
  <h1>The ENDOSCOPE <em>Expert</em></h1>
  <p class="abs sub center">We repair, buy and sell Top Endoscopy Equipment Manufacturers</p>
  <p class="abs cert">
    <svg width="20" height="20" viewBox="0 0 20 20"><circle cx="10" cy="10" r="8.5" fill="none" stroke="#fff" stroke-width="1.5"/><path d="M6 10.3l2.7 2.7L14 7.5" fill="none" stroke="#fff" stroke-width="1.6"/></svg>
    Certified ISO 9001
  </p>
  <a class="abs btn-white center">Repair Now</a>
  <a class="abs services center">Our Services</a>
</section>

<section class="abs brands">
  <p class="abs lead">We've got you covered:</p>
  <span class="abs brandname" style="left:395px;top:24px;font-size:22px">KAMIRO</span>
  <span class="abs brandname" style="left:590px;top:14px;font-size:22px">VELTRA<br><span style="font-size:16px;font-weight:400;padding-left:12px">MEDICAL</span></span>
  <span class="abs brandname" style="left:792px;top:24px;font-size:22px">ORIMAX</span>
</section>

<section class="expert">
  <h2 class="abs section center" style="top:912px;width:1200px">Our Expertise</h2>

  <div class="col" style="left:171px;top:1034px">
    <svg width="70" height="70" viewBox="0 0 70 70"><g fill="none" stroke="#2aaaf4" stroke-width="2.5"><circle cx="30" cy="36" r="24"/><circle cx="30" cy="36" r="16"/><circle cx="30" cy="36" r="8"/><path d="M30 36h34M56 30l8 6-8 6"/></g></svg>
    <h3>Endoscope repair service</h3>
    <p>Manufacturer-independent we repair and maintain endoscopes, individual components, accessories and peripherals of the manufacturers Orimax, Veltra and Kamiro.</p>
  </div>
  <div class="col" style="left:480px;top:1034px">
    <svg width="70" height="70" viewBox="0 0 70 70"><g fill="none" stroke="#2aaaf4" stroke-width="2.5"><path d="M64 18H8M18 8L8 18l10 10"/><path d="M6 52h56M52 42l10 10-10 10"/></g><g stroke="#2aaaf4" stroke-width="2"><path d="M28 34h30M20 34h4"/></g></svg>
    <h3>Used endoscopes</h3>
    <p>Our regular stock includes refurbished gastroscopes, coloscopes, bronchoscopes, cystoscopes and duodenoscopes from the well-known manufacturers Orimax, Veltra and Kamiro.</p>
  </div>
  <div class="col" style="left:789px;top:1034px">
    <svg width="70" height="70" viewBox="0 0 70 70"><g fill="none" stroke="#2aaaf4" stroke-width="2.5"><circle cx="46" cy="22" r="16"/><path d="M50 14h-6a3.5 3.5 0 000 7h4a3.5 3.5 0 010 7h-7M46 10v4M46 28v4"/><path d="M8 40h10v24H8zM18 44l8-10 4 2-2 8h12a3 3 0 010 6h-2a3 3 0 010 6h-4a3 3 0 010 6H18"/></g></svg>
    <h3>Used endoscopes</h3>
    <p>We are very interested in buying your old endoscopes – even defective and dismantled! We offer fair conditions! Please contact us for a purchase offer!</p>
  </div>

  <a class="pill navy" style="left:195px;top:1292px;width:189px;height:31px">REPAIR HERE <span>→</span></a>
  <a class="pill navy" style="left:511px;top:1292px;width:179px;height:31px">SELL IT NOW <span>→</span></a>
  <a class="pill navy" style="left:823px;top:1292px;width:171px;height:31px">BUY IT USED <span>→</span></a>
</section>

<section class="abs about">
  <svg class="abs warranty" style="left:128px;top:51px" viewBox="0 0 268 66">
    <text x="0" y="62" font-family="Josefin Sans, sans-serif" font-weight="700" font-style="normal" font-size="78" fill="#2aaaf4">12</text>
    <rect x="100" y="0" width="168" height="32" fill="#15206b"/>
    <rect x="100" y="34" width="168" height="32" fill="#2aaaf4"/>
    <text x="116" y="22" font-family="Josefin Sans, sans-serif" font-weight="700" font-size="18" fill="#fff">MONTHS</text>
    <text x="116" y="57" font-family="Josefin Sans, sans-serif" font-weight="700" font-size="18" fill="#fff">WARRANTY</text>
  </svg>
  <h2 class="abs" style="top:138px">Lumen<span>FIX</span> GmbH</h2>
  <p class="abs tag" style="top:190px">We repair, Buy and sale</p>
  <div class="abs body" style="top:230px">
    <p>Specialised in the repair and sale of Orimax, Veltra and Kamiro flexible medical endoscopes. As a service-oriented company, we are certified according to DIN ISO 9001:2015 and we are at your side with our knowledge and skills!</p>
    <p style="margin-top:19px">LumenFix is a privileged partner for the start-up facility or optimisation of existing healthcare facilities, doctor's offices and hospitals. The quality and reliability of our products and our offered service are our best advertisement! We provide high and consistent quality by monitoring all processes. Convince yourself!</p>
  </div>
  <div class="photo" role="img" aria-label="Photo of a black endoscope control body with eyepiece" style="left:619px;top:66px;width:581px;height:262px;background:radial-gradient(ellipse at 50% 55%,#9a9a9a 0%,#5a5a5a 30%,#e0e0e0 65%,#ececec 100%)"></div>
  <span class="abs brandname" style="left:612px;top:422px;font-size:21px">KAMIRO</span>
  <span class="abs brandname" style="left:808px;top:408px;font-size:22px">VELTRA<br><span style="font-size:16px;font-weight:400;padding-left:12px">MEDICAL</span></span>
  <span class="abs brandname" style="left:1010px;top:420px;font-size:21px">ORIMAX</span>
</section>

<!-- Repair -->
<div class="feature" style="left:51px;top:2068px;width:467px;height:379px;background:var(--card);padding-left:77px">
  <svg width="70" height="66" viewBox="0 0 70 66" style="margin-top:-24px;margin-left:-4px"><g fill="none" stroke="#2aaaf4" stroke-width="2.5"><circle cx="30" cy="33" r="24"/><circle cx="30" cy="33" r="16"/><circle cx="30" cy="33" r="8"/><path d="M30 33h34M56 27l8 6-8 6"/></g></svg>
  <h3 style="margin-top:8px">We Repair Endoscopes,</h3>
  <h4>Systems, parts, Components and Accessories</h4>
  <p>Manufacturer-independent we repair and maintain endoscopes, individual components, accessories and peripherals of the manufacturers Orimax, Veltra and Kamiro.</p>
</div>
<a class="pill sky" style="left:128px;top:2387px;width:234px;height:30px;justify-content:space-between;padding:0 20px 0 58px">REPAIR NOW <span>→</span></a>
<div class="photo" role="img" aria-label="Photo of endoscopes and mouth guards on a blue table" style="left:551px;top:2068px;width:649px;height:379px;background:linear-gradient(135deg,#d9a64a 0%,#6fb3c9 35%,#3d8fb0 70%,#2b6c8c 100%)"></div>

<!-- Purchase -->
<div class="photo" role="img" aria-label="Photo of a technician inspecting an endoscope beside a video tower" style="left:0;top:2571px;width:549px;height:377px;background:linear-gradient(90deg,#dfe2e5 0%,#c8cdd2 45%,#eef0f2 100%)"></div>
<div class="feature" style="left:551px;top:2571px;width:649px;height:377px;background:var(--pale);padding-left:64px">
  <svg width="70" height="66" viewBox="0 0 70 66" style="margin-top:-24px;margin-left:-4px"><g fill="none" stroke="#2aaaf4" stroke-width="2.5"><circle cx="30" cy="33" r="24"/><circle cx="30" cy="33" r="16"/><circle cx="30" cy="33" r="8"/><path d="M30 33h34M56 27l8 6-8 6"/></g></svg>
  <h3 style="margin-top:8px">We Purchase Endoscopes,</h3>
  <h4>Components and Accessories</h4>
  <p>Manufacturer-independent we repair and maintain endoscopes, individual components, accessories and peripherals of the manufacturers Orimax, Veltra and Kamiro.</p>
</div>
<a class="pill navy" style="left:615px;top:2886px;width:307px;height:31px;justify-content:space-between;padding:0 20px 0 60px">SELL YOUR ENDOSCOPE <span>→</span></a>

<!-- Sell -->
<div class="feature" style="left:51px;top:3064px;width:467px;height:378px;background:var(--card);padding-left:77px">
  <svg width="70" height="66" viewBox="0 0 70 66" style="margin-top:-24px;margin-left:-4px"><g fill="none" stroke="#2aaaf4" stroke-width="2.5"><circle cx="30" cy="33" r="24"/><circle cx="30" cy="33" r="16"/><circle cx="30" cy="33" r="8"/><path d="M30 33h34M56 27l8 6-8 6"/></g></svg>
  <h3 style="margin-top:8px">We Sell Endoscopes,</h3>
  <h4>Components and Accessories</h4>
  <p>Manufacturer-independent we repair and maintain endoscopes, individual components, accessories and peripherals of the manufacturers Orimax, Veltra and Kamiro.</p>
</div>
<a class="pill coral" style="left:128px;top:3382px;width:234px;height:30px;justify-content:space-between;padding:0 20px 0 77px">BUY NOW <span>→</span></a>
<div class="photo" role="img" aria-label="Photo of an endoscopy light source unit with control panel" style="left:551px;top:3064px;width:649px;height:378px;background:linear-gradient(135deg,#f3b39c 0%,#e7e9ee 30%,#5a6a94 60%,#1f2a52 100%)"></div>

<section class="abs values">
  <h2 class="abs center">Our Values</h2>
  <div class="val" style="left:99px">
    <svg width="70" height="70" viewBox="0 0 70 70"><circle cx="35" cy="35" r="31" fill="none" stroke="#fff" stroke-width="4"/><path d="M21 36l10 10 18-20" fill="none" stroke="#fff" stroke-width="4.5"/></svg>
    <h3>Cost Efficient</h3>
    <p>Manufacturer-independent we repair and maintain endoscopes, individual components, accessories and peripherals of the manufacturers Orimax, Veltra and Kamiro.</p>
  </div>
  <div class="val" style="left:429px">
    <svg width="70" height="70" viewBox="0 0 70 70"><circle cx="35" cy="35" r="31" fill="none" stroke="#fff" stroke-width="4"/><path d="M21 36l10 10 18-20" fill="none" stroke="#fff" stroke-width="4.5"/></svg>
    <h3>No Maintenance Contract</h3>
    <p>Our regular stock includes refurbished gastroscopes, coloscopes, bronchoscopes, cystoscopes and duodenoscopes from the well-known manufacturers Orimax, Veltra and Kamiro.</p>
  </div>
  <div class="val" style="left:808px">
    <svg width="70" height="70" viewBox="0 0 70 70"><circle cx="35" cy="35" r="31" fill="none" stroke="#fff" stroke-width="4"/><path d="M21 36l10 10 18-20" fill="none" stroke="#fff" stroke-width="4.5"/></svg>
    <h3>German Quality</h3>
    <p>We are very interested in buying your old endoscopes – even defective and dismantled! We offer fair conditions! Please contact us for a purchase offer!</p>
  </div>
</section>

<section class="contact">
  <svg class="abs" style="left:290px;top:4186px" width="50" height="36" viewBox="0 0 50 36"><g fill="none" stroke="#c8c8c8" stroke-width="2"><rect x="2" y="2" width="46" height="32"/><path d="M2 2l23 18L48 2M2 34l17-15M48 34L31 19"/></g></svg>
  <h2 class="abs" style="left:13px;top:4270px">Faulty Endoscope?</h2>
  <p class="abs" style="left:13px;top:4329px">Discover classic and brand new styles in a variety of<br>shapes, colours and materials, from signature Frame<br>to the latest teardrop inspired watches.</p>
  <a class="cbtn" style="left:81px">CONTACT US</a>

  <div class="abs" style="left:601px;top:4228px;width:2px;height:235px;background:#2aaaf4"></div>

  <svg class="abs" style="left:868px;top:4180px" width="60" height="50" viewBox="0 0 60 50"><path d="M10 4c-4 2-7 6-5 13 3 10 11 20 21 26 6 3 11 2 13-2l-6-7c-2 1-4 2-6 1-5-3-10-9-12-15 0-2 1-4 3-5L12 4z" fill="#cfcfcf"/><path d="M34 6a14 14 0 0110 12M38 0a20 20 0 0114 16" fill="none" stroke="#cfcfcf" stroke-width="2.5"/></svg>
  <h2 class="abs" style="left:597px;top:4270px">Call Us</h2>
  <p class="abs" style="left:597px;top:4329px">+49 4000 555 010-0</p>
  <p class="abs" style="left:597px;top:4356px">Monday - Friday<br>8AM - 20AM UTC</p>
  <a class="cbtn" style="left:666px">CALL NOW</a>
</section>

<footer>
  <div class="abs brand" style="left:548px;top:4590px"><i></i>LumenFix</div>
  <i class="social" style="left:564px"></i>
  <i class="social" style="left:599px"></i>
  <i class="social" style="left:634px"></i>
  <i class="abs" style="left:560px;top:4719px;width:22px;height:15px;background:linear-gradient(#000 0 33%,#dd0000 33% 66%,#ffce00 66%)"></i>
  <div class="abs" style="left:614px;top:4712px;width:54px;height:30px;border-radius:15px;background:#eceff6"></div>
  <i class="flag" style="left:631px;top:4720px"></i>
  <div class="abs" style="left:73px;top:4758px;width:52px;height:34px;background:#2a4a9a"></div>
  <span class="abs" style="left:141px;top:4772px;font-size:10px;color:#777">info@lumenfix.example</span>
  <nav class="abs foot-links"><a>Home</a><a>Repair</a><a>Buy</a><a>Sell</a><a>pick-up order</a><a>about us</a><a>contact us</a></nav>
  <span class="abs" style="left:1166px;top:4750px;font-size:12px;color:#999">↑</span>
  <p class="abs copyright">Copyright © 2022 LumenFix GmbH. Use of this website constitutes acceptance of our User Agreement and Privacy Policy.</p>
</footer>

</body>
</html>
```